Morvetta Designs - Online Shoe Shop

Morvetta is an online shoes and bags shop. We sell Imported Genuine Leather shoes and bags our market is LSM 8-10. We mainly sell women shoes and bags and we will also be introducing men’s shoes and belts.
I would like a website design and development that is responsive, clean, elegant and easy to use. Where customers can make a purchase online.
Have CATEGORIES in SHOE STYLE (i.e. Heels, Sandals, Pumps, Mules, Boots, Sneaker, Flats, etc) and PRICE RANGE should be in South African Rands currency, COLOUR, SIZE.
For shoe images we should be able to add videos as well.
Header and Footer Menu should have the basic menu list. Header Menu (New Arrivals, Preorder, Women’s Collection, Men’s Collection, Summer 2020 Collection, Winter 2020 Collection, Bags, Accessories, Sale, etc
Auto display when the item is SOLD OUT. Add an option for a user to get notification on when the item is back in stock.
Icons to show when shoes are on sale and Show was and now price.
Users to be able to review and rate the items.
Discount codes for new email subscribers.
Consumers should be able to pay using different options, Credit card, QuidLane, EFT, etc
Add an option for discount coupons at checkout.
After placing and order they should receive an email with order receipt.
Site should have a shipping and tracking option. International shipping such as KRT and BOLTAIR. For local shipping in South Africa please add Quickpath Couriers and Zenobi Couriers.
Backend: Backend should be easy to add more categories, items and changing header banners, adding sale alerts. To get notification when the stock is low and sold out. Get notification when an order is placed online so to prepare packing for shipping.
Can we make sure that the SEO is in place and bare in mind all searchy rules to avoid being penalized.
Target Market(s)
Women from age 25-65
LSM 8-10
Entire South Africa and neighboring countries
Industry/Entity Type
Shoe Store
Coding
Coded - Design and coding required
Number of Pages Required
5+ page
Requirements
Must have
- Responsive
Clean
Modern
Shopping cart
Shipping options integration
Newsletter subscription
Social media icons
Nice to have
- The business colors are Gold and White or Gold and Black

```html
<!DOCTYPE html>
<html lang="en">
<head>
<meta charset="utf-8">
<title>Morvetta Designs — Hand Bags</title>
<link href="https://fonts.googleapis.com/css2?family=Poppins:wght@400;500;600&family=Playfair+Display:ital,wght@0,400;0,700;1,400&display=swap" rel="stylesheet">
<style>
:root{
  --gold:#c9a14a;
  --dark:#1e1e1e;
  --ink:#333;
  --muted:#8a8a8a;
  --line:#e6e6e6;
  --soft:#f4f4f4;
  --band:#e9e9e9;
  --white:#fff;
}
*{box-sizing:border-box;margin:0;padding:0}
html,body{width:1200px;height:2284px;overflow:hidden}
body{font-family:"Poppins",sans-serif;color:var(--ink);background:var(--white);font-size:12px;position:relative}
.wrap{width:920px;margin:0 auto;position:relative}

/* top bar */
.topbar{height:40px;background:var(--dark);color:#ddd;font-size:10px}
.topbar .wrap{display:flex;align-items:center;justify-content:space-between;height:40px}
.dots{display:flex;gap:8px}
.dots span{width:12px;height:12px;border-radius:50%;background:#777}
.contact-line{display:flex;gap:26px;letter-spacing:.5px}
.contact-line b{color:var(--gold);font-weight:500}

/* header */
.header{height:92px}
.header .wrap{display:flex;align-items:center;justify-content:space-between;height:92px}
.brand{display:flex;align-items:center;gap:10px}
.brand i{width:30px;height:30px;background:var(--dark);border-radius:50%;display:block}
.brand span{font-size:20px;font-weight:600;color:var(--dark)}
.tagline{font-family:"Playfair Display",serif;font-style:italic;font-size:16px;color:var(--ink);text-align:center;line-height:1.3}
.tagline small{display:block;font-family:"Poppins",sans-serif;font-style:normal;font-size:9px;color:var(--muted)}
.search-cart{display:flex;align-items:center;gap:16px}
.search{width:200px;height:30px;border:1px solid var(--line);display:flex;align-items:center;justify-content:space-between;padding:0 10px;color:var(--muted);font-size:10px}

/* nav */
.nav{height:46px;border-top:1px solid var(--line);border-bottom:1px solid var(--line)}
.nav ul{list-style:none;display:flex;gap:30px;height:44px;align-items:center;font-size:10px;font-weight:500;letter-spacing:.4px}
.nav li.active{color:var(--gold)}

/* page banner */
.page-banner{margin-top:70px;height:100px;background:var(--band)}
.page-banner .wrap{display:flex;align-items:center;justify-content:space-between;height:100px;width:880px}
.page-banner h1{font-size:12px;font-weight:600;letter-spacing:1px}
.banner-bag{position:absolute;left:410px;top:-6px;width:60px;height:92px;border-radius:8px 8px 12px 12px;background:linear-gradient(160deg,#a86d3c,#6b3f1e)}
.crumb{font-size:10px;color:var(--muted)}

/* main */
.main{width:880px;margin:60px auto 0;display:flex;justify-content:space-between}
.sidebar{width:152px}
.side-box{border:1px solid var(--line);padding:18px 14px;margin-bottom:26px}
.side-box h3{font-size:12px;font-weight:600;margin-bottom:12px}
.side-box ul{list-style:none;font-size:10px;color:var(--muted);line-height:26px}
.side-box li::before{content:"";display:inline-block;width:8px;height:8px;border:1px solid #bbb;margin-right:8px;vertical-align:-1px}
.side-box h4{font-size:10px;font-weight:500;margin:12px 0 4px}
.best h3{font-size:12px;font-weight:600;margin:6px 0 14px}
.best .shoe{height:180px;background:linear-gradient(180deg,#fff 20%,#e8ecf2 55%,#3b4a66);border:1px solid var(--line)}
.best .name{font-family:"Playfair Display",serif;text-align:center;margin-top:14px;font-size:12px}
.best .price{text-align:center;font-weight:600;font-size:12px;margin-top:4px}
.promo{margin-top:26px;height:250px;background:linear-gradient(180deg,#dcdcdc,#8a8a8a 45%,#222);color:#fff;text-align:center;display:flex;flex-direction:column;justify-content:flex-end;padding-bottom:20px;font-size:10px;line-height:1.6}
.promo b{font-size:12px;font-weight:600;letter-spacing:.5px}

.content{width:660px}
.toolbar{display:flex;justify-content:space-between;align-items:center;height:28px;font-size:10px;color:var(--muted)}
.views{display:flex;gap:6px}
.views span{width:16px;height:16px;border:1px solid #bbb}
.views span:first-child{background:#555}
.sorts{display:flex;gap:18px;align-items:center}
.select{border:1px solid var(--line);padding:3px 10px;display:inline-block;width:70px;color:var(--ink)}
.grid{margin-top:40px;display:grid;grid-template-columns:repeat(3,200px);column-gap:30px;row-gap:70px}
.card .photo{height:200px;border:1px solid var(--line);padding:18px}
.card .photo div{width:100%;height:100%}
.brown{background:radial-gradient(ellipse 48% 42% at 50% 55%,#8a5a33 0,#a97447 55%,#fff 100%)}
.grey{background:radial-gradient(ellipse 40% 46% at 50% 55%,#cfcfcf 0,#e2e2e2 60%,#fff 100%)}
.silver{background:radial-gradient(ellipse 46% 40% at 50% 55%,#b4b4b4 0,#d2d2d2 60%,#fff 100%)}
.stars{text-align:center;color:#ccc;font-size:11px;letter-spacing:2px;margin-top:14px}
.card .name{font-family:"Playfair Display",serif;text-align:center;font-size:13px;margin-top:4px}
.card .price{text-align:center;font-weight:600;font-size:12px;margin-top:3px}
.showing{text-align:right;font-size:10px;color:var(--muted);margin-top:100px}

/* footer */
.footer-area{position:absolute;left:0;top:1660px;width:1200px;height:440px;background:var(--soft)}
.footer-card{width:880px;margin:36px auto 0;background:var(--white);height:368px;display:flex;justify-content:space-between;padding:48px 46px}
.f-col h3{font-size:14px;font-weight:500;letter-spacing:1px;margin-bottom:22px}
.f-col ul{list-style:none;font-size:11px;color:var(--muted);line-height:28px}
.f-col li::before{content:"› "}
.f-info{width:200px}
.f-news{width:330px;text-align:center;padding-top:14px}
.f-news h3{font-family:"Playfair Display",serif;font-size:26px;letter-spacing:4px;font-weight:400}
.f-news p{font-size:11px;color:var(--muted);line-height:19px}
.sub{margin:30px auto 0;width:270px;height:40px;border:1px solid var(--line);border-radius:20px;display:flex;align-items:center;justify-content:space-between;padding-left:16px;font-size:10px;color:var(--muted)}
.sub span{width:32px;height:32px;border-radius:50%;background:var(--dark);margin-right:3px;display:flex;align-items:center;justify-content:center}
.f-contact{width:200px;font-size:11px;color:var(--muted);line-height:21px}
.f-contact p{margin-bottom:14px}
.bottom{position:absolute;left:0;top:2100px;width:1200px;height:184px;background:var(--white)}
.bottom .wrap{width:880px;display:flex;justify-content:space-between;align-items:center;height:80px;font-size:10px;color:var(--muted)}
.pay{display:flex;gap:10px;align-items:center}
.pay b{font-weight:600;color:var(--dark)}
.find{display:flex;gap:6px;align-items:center}
.find span{width:11px;height:11px;border-radius:50%;background:#999}
.foot-nav{border-top:1px solid var(--line);height:60px}
.foot-nav ul{width:880px;margin:0 auto;list-style:none;display:flex;justify-content:space-between;align-items:center;height:60px;font-size:10px;font-weight:500;color:var(--muted);letter-spacing:.4px}
</style>
</head>
<body>

<div class="topbar"><div class="wrap">
  <div class="dots"><span></span><span></span><span></span></div>
  <div class="contact-line"><span>TOLL FREE: <b>(010) 555 0100</b></span><span>MAIL INFO: <b>hello@morvetta.example</b></span></div>
</div></div>

<header class="header"><div class="wrap">
  <div class="brand"><i></i><span>Morvetta</span></div>
  <div class="tagline">Discount sales for your loyal subscribers<small>Genuine leather shoes and bags, shipped nationwide</small></div>
  <div class="search-cart">
    <div class="search">Search<svg width="11" height="11" viewBox="0 0 12 12"><circle cx="5" cy="5" r="4" fill="none" stroke="#888" stroke-width="1.4"/><path d="M8 8l3 3" stroke="#888" stroke-width="1.4"/></svg></div>
    <svg width="24" height="22" viewBox="0 0 24 22"><path d="M1 2h4l3 12h12l3-9H7" fill="none" stroke="#c9a14a" stroke-width="2"/><circle cx="10" cy="19" r="2" fill="#c9a14a"/><circle cx="18" cy="19" r="2" fill="#c9a14a"/></svg>
  </div>
</div></header>

<nav class="nav"><div class="wrap"><ul>
  <li class="active">HOME</li><li>NEW ARRIVALS</li><li>PRE ORDER</li><li>MEN COLLECTION</li><li>WOMEN COLLECTION</li><li>SEASON COLLECTIONS</li><li>BAGS</li><li>ACCESSORIES</li>
</ul></div></nav>

<section class="page-banner"><div class="wrap">
  <h1>HAND BAGS</h1>
  <div class="banner-bag" role="img" aria-label="Brown leather handbag"></div>
  <div class="crumb">⌂ › Handbags</div>
</div></section>

<div class="main">
  <aside class="sidebar">
    <div class="side-box">
      <h3>Categories</h3>
      <ul><li>Bags</li><li>Accessories</li><li>Shoes</li><li>Collections</li><li>Loafer</li><li>Sneakers</li><li>Heels</li><li>Flats</li></ul>
    </div>
    <div class="side-box">
      <h3>Refine Search</h3>
      <h4>Manufacturer</h4>
      <ul><li>Leather</li><li>Suede</li></ul>
      <h4>Price Range</h4>
      <ul><li>R0 - R500</li><li>R500 - R1000</li><li>R1000 - R2000</li><li>R2000 - R3000</li></ul>
    </div>
    <div class="best">
      <h3>Best Seller</h3>
      <div class="shoe" role="img" aria-label="Navy leather ankle bootie"></div>
      <div class="name">Product Name</div>
      <div class="price">$100.00</div>
    </div>
    <div class="promo" role="img" aria-label="Runway model promotion for the cat walk collection">
      <span>New Season</span><b>CAT WALK COLLECTION</b><span>Starting from $99.00</span>
    </div>
  </aside>

  <section class="content">
    <div class="toolbar">
      <div class="views"><span></span><span></span></div>
      <div class="sorts"><span>Sort by: <span class="select">Default</span></span><span>Show: <span class="select" style="width:40px">9</span></span></div>
    </div>
    <div class="grid">
      <div class="card"><div class="photo"><div class="brown" role="img" aria-label="Brown leather saddle bag"></div></div><div class="stars">★★★★★</div><div class="name">Product Name</div><div class="price">$100.00</div></div>
      <div class="card"><div class="photo"><div class="grey" role="img" aria-label="Grey leather tote bag"></div></div><div class="stars">★★★★★</div><div class="name">Product Name</div><div class="price">$100.00</div></div>
      <div class="card"><div class="photo"><div class="silver" role="img" aria-label="Silver leather handbag"></div></div><div class="stars">★★★★★</div><div class="name">Product Name</div><div class="price">$100.00</div></div>
      <div class="card"><div class="photo"><div class="brown" role="img" aria-label="Brown leather saddle bag"></div></div><div class="stars">★★★★★</div><div class="name">Product Name</div><div class="price">$100.00</div></div>
      <div class="card"><div class="photo"><div class="grey" role="img" aria-label="Grey leather tote bag"></div></div><div class="stars">★★★★★</div><div class="name">Product Name</div><div class="price">$100.00</div></div>
      <div class="card"><div class="photo"><div class="silver" role="img" aria-label="Silver leather handbag"></div></div><div class="stars">★★★★★</div><div class="name">Product Name</div><div class="price">$100.00</div></div>
      <div class="card"><div class="photo"><div class="brown" role="img" aria-label="Brown leather saddle bag"></div></div><div class="stars">★★★★★</div><div class="name">Product Name</div><div class="price">$100.00</div></div>
      <div class="card"><div class="photo"><div class="grey" role="img" aria-label="Grey leather tote bag"></div></div><div class="stars">★★★★★</div><div class="name">Product Name</div><div class="price">$100.00</div></div>
      <div class="card"><div class="photo"><div class="silver" role="img" aria-label="Silver leather handbag"></div></div><div class="stars">★★★★★</div><div class="name">Product Name</div><div class="price">$100.00</div></div>
    </div>
    <div class="showing">Showing 1 to 9 of 9</div>
  </section>
</div>

<footer class="footer-area">
  <div class="footer-card">
    <div class="f-col f-info">
      <h3>INFORMATION</h3>
      <ul><li>About Us</li><li>Delivery Information</li><li>Privacy Policy</li><li>Terms &amp; Conditions</li><li>Returns &amp; Exchanges</li><li>Highlights</li><li>Contact Us</li></ul>
    </div>
    <div class="f-col f-news">
      <h3>NEWSLETTER</h3>
      <p>Subscribe to our newsletter to get notified about all the fresh leather arrivals. Discount codes for new email subscribers.</p>
      <div class="sub">Enter your email address<span><svg width="10" height="10" viewBox="0 0 10 10"><path d="M1 5h7M5 2l3 3-3 3" stroke="#c9a14a" stroke-width="1.5" fill="none"/></svg></span></div>
    </div>
    <div class="f-col f-contact">
      <h3 style="color:var(--ink)">CONTACT US</h3>
      <p>12 Loop Street, Gardens<br>Cape Town 8001<br>South Africa</p>
      <p>(010) 555 0100<br>(010) 555 0101</p>
      <p>hello@morvetta.example</p>
    </div>
  </div>
</footer>

<div class="bottom">
  <div class="wrap">
    <div class="pay">Pay Via <b>Cardeon</b><b>Varsa</b><b>QuidLane</b></div>
    <div>Powered By Morvetta © 2020</div>
    <div class="find">Find Us At <span></span><span></span><span></span><span></span></div>
  </div>
  <nav class="foot-nav"><ul>
    <li>HOME</li><li>NEW ARRIVALS</li><li>PRE ORDER</li><li>MEN COLLECTION</li><li>WOMEN COLLECTION</li><li>SEASON COLLECTIONS</li><li>BAGS</li><li>ACCESSORIES</li>
  </ul></nav>
</div>

</body>
</html>
```